The Bramblewood Roadside Defense Guide
An Owner's Notes on Quietly Settling Every Old Dispute
The Bramblewood Roadside Defense Guide - Law
This book will be read by middle class, well educated people with pending reckless driving charges.
Dimensions are approximately 6.5" x 8.5" (half sheet). We would like the title, sub title and the author's name ( Owen T. Marsh) to appear on the front cover. No text on the spine (about 1/8" spine). The back page will have no text. but the design on the back cover should allow us to place a text layer on top of the back cover design - so the back cover design should not make it difficult to read the text. (See attached example from previous project)
omarsh omarsh
#99 #100 #101 Submissions should not have any text on the back cover. Please remove the text from the back cover if you want your submission to be considered.
#61 - Can you do some variations of the text. Perhaps tweak the color or the color gradient.
#36 #66 #61 #45 #42 #53 #45 These are the top contenders. These are all awesome designs! To be selected the design must include back and front covers and NOT contain "2nd edition"
#36 #66 #61 #45 To be considered you must have a back cover as well as a front cover. Please resubmit your design with a back cover
#61 Can you take off the "2nd edition" from the front - this is not the second edition.
#14 my wife likes this one so that is a plus.:)
#7 this looks like a book on Velvet Harbor - Awesome! but probably not a great angle for a law firm :) I wonder if they would sue me if we just put a crystal pyramid and rainbow on the cover?
#11 nice design but too similar to the DUI book cover.
#14 Reckless driving cases are 80% speed related so the cover matches the subject well and it breaks away from the frame clip art pack nicely. The is something about it that says "Car ad" rather than legal book though. Maybe its the bright colors and contemporary "smart car" looking vehicle. May be look for different versions of the same theme and see.
#23 - forgot the title.
#20 I like the dirty scratched texture you did in #8 better, it makes it seem more interesting. #8's texturing is pretty heavy though, a slightly toned version, something in between #8 and #20 might be a good idea, no 100% sure though. I still think there needs to be some original graphic on the cover instead of just the text or framed clip art.
#9 I like that you are creating original images instead of just using the clip art whole-cloth and getting rid of the borders. That doesn't mean that a submission couldn't have a square frame clip art, it just means that originality scores points.
#22 Not bad, but the simplicity takes away from the professionalism. The look is not bad but then you realize its just swirled sirens with the clip art pasted on top. If the cover image was something original or it used some original elements in it I think it would help overcome that. I really like that your submissions are all over the place and not just a different versions of the same thing.
#19 I like that concept of this design. Its abstract, not just clip art photography pastes on the cover. Its completely unique from the other too examples of book covers. The colors and text are not my favorite. So the execution is not there yet but the fact that it is completely going off on its own is a big plus.
#8 I like the design of the scratched surface and the yellow hash marks...but it seems a little off. I don't know that the clip art I uploaded really matches. I can't help but wonder if something with traffic cones or a speed limit sign might be better. Don't know for sure...just vague impressions.
#21 this looks too similar to what we already have and is not very contemporary. Keep trying though.
#18 is a bit too similar to the DUI book cover I uploaded as an example. I don't want to be derivative.
#1 I think the police tap doesn't really match the Reckless driving. Most reckless driving cases are for speeding or minor car accidents, falling asleep at the wheel or someone doing doughnuts in a parking lot. Police crime scene tape doesn't usually come into play.
#2,#,3,#4 I marked these low because this is a reckless driving book not DUI. Reckless driving is not generally an alcohol offense in Va and so the covers' designs were a bit confusing.

```html
<!DOCTYPE html>
<html lang="en">
<head>
<meta charset="utf-8">
<title>The Bramblewood Roadside Defense Guide</title>
<link rel="stylesheet" href="https://fonts.googleapis.com/css2?family=Libre+Baskerville:wght@400;700&display=swap">
<style>
  :root {
    --asphalt: #1a1a18;
    --asphalt-deep: #0d0d0c;
    --paint-yellow: #e2a516;
    --paint-yellow-light: #f0bd3a;
    --paint-yellow-dark: #b98410;
    --title-gold: #e9b93a;
    --title-gold-dark: #b57e17;
    --cover-white: #f4f1ea;
    --cone-orange: #ef6a1f;
  }
  html, body {
    margin: 0;
    padding: 0;
    width: 1200px;
    height: 917px;
    overflow: hidden;
    background: var(--asphalt);
  }
  .cover {
    position: relative;
    width: 1200px;
    height: 917px;
    overflow: hidden;
    background: var(--asphalt);
    font-family: "Libre Baskerville", "Times New Roman", serif;
  }
  .hazard-stripes {
    position: absolute;
    left: 0;
    top: 0;
    width: 1200px;
    height: 236px;
    display: block;
  }
  .title-band {
    position: absolute;
    left: 0;
    top: 236px;
    width: 1200px;
    height: 199px;
    background: linear-gradient(180deg, var(--asphalt-deep), var(--asphalt));
  }
  .painted-road {
    position: absolute;
    left: 0;
    top: 435px;
    width: 1200px;
    height: 285px;
    background: radial-gradient(ellipse at 40% 50%, var(--paint-yellow-light), var(--paint-yellow) 55%, var(--paint-yellow-dark));
  }
  .lower-band {
    position: absolute;
    left: 0;
    top: 720px;
    width: 1200px;
    height: 197px;
    background: linear-gradient(180deg, var(--asphalt), var(--asphalt-deep));
  }
  .book-title {
    position: absolute;
    left: 640px;
    top: 262px;
    width: 660px;
    margin: 0;
    text-align: center;
    text-transform: uppercase;
    font-weight: 700;
    line-height: 1.15;
    color: var(--title-gold);
    background: linear-gradient(180deg, var(--title-gold) 40%, var(--title-gold-dark));
    -webkit-background-clip: text;
    background-clip: text;
    -webkit-text-fill-color: transparent;
  }
  .book-title .line-small { display: block; font-size: 36px; }
  .book-title .line-large { display: block; font-size: 54px; letter-spacing: 1px; }
  .traffic-cones {
    position: absolute;
    left: 720px;
    top: 440px;
    width: 280px;
    height: 255px;
    border-radius: 20px;
    background: radial-gradient(ellipse at 50% 55%, var(--cone-orange), rgba(239,106,31,0.35) 60%, rgba(239,106,31,0));
  }
  .subtitle {
    position: absolute;
    left: 520px;
    top: 738px;
    width: 760px;
    margin: 0;
    text-align: center;
    text-transform: uppercase;
    font-weight: 700;
    font-size: 17px;
    line-height: 1.95;
    color: var(--cover-white);
  }
  .subtitle span { display: block; }
  .author {
    position: absolute;
    left: 520px;
    top: 847px;
    width: 760px;
    margin: 0;
    text-align: center;
    font-size: 25px;
    color: var(--cover-white);
  }
</style>
</head>
<body>
<div class="cover">
  <svg class="hazard-stripes" viewBox="0 0 1200 236" xmlns="http://www.w3.org/2000/svg" aria-hidden="true">
    <rect width="1200" height="236" fill="#141412"/>
    <g fill="#e2a516">
      <polygon points="-150,236 -40,236 110,0 0,0"/>
      <polygon points="70,236 180,236 330,0 220,0"/>
      <polygon points="290,236 400,236 550,0 440,0"/>
      <polygon points="510,236 620,236 770,0 660,0"/>
      <polygon points="730,236 840,236 990,0 880,0"/>
      <polygon points="950,236 1060,236 1210,0 1100,0"/>
      <polygon points="1170,236 1280,236 1430,0 1320,0"/>
    </g>
  </svg>
  <div class="title-band"></div>
  <div class="painted-road" role="img" aria-label="Cracked yellow-painted asphalt road surface"></div>
  <div class="lower-band"></div>

  <h1 class="book-title">
    <span class="line-small">The Bramblewood</span>
    <span class="line-small">Roadside Defense</span>
    <span class="line-large">Guide</span>
  </h1>

  <div class="traffic-cones" role="img" aria-label="Two orange and white traffic cones, one standing and one tipped over"></div>

  <p class="subtitle">
    <span>An Owner's Notes on Quietly</span>
    <span>Settling Every Old Dispute</span>
  </p>

  <p class="author">Owen T. Marsh</p>
</div>
</body>
</html>
```